Business Card Design Project

We need a business card design template for a direct sales company that is branded to the company but the name information can be changed for the representatives. The card needs to include the company logo and website...www.myvelsane.example. It should also include the Customer Service number which is 1-800-472-Velsan.

The front should have a space with the name and a place for their phone contact information and email address.
Updates

The card should be two sided.  It could also include the tagline "Velsane is all about V!" or any of the information from www.myvelsane.example.

I am uploading the other formats that I currently have for the logo.

Thank you

Target Market(s)

The representatives are teenage girls that are 13-19 but they are selling products to all ages.

Industry/Entity Type

Business

Requirements
Must have
• A field with the toll free customer service number.
The company logo.
The company website information.
The company representative name.
The company representative phone number.
The company representative email contact info.
Nice to have
• QR Code which we already have.
Should not have
• Do not make it look like a design for children. It should be modern and professional but sophisticated.

```html
<!DOCTYPE html>
<html lang="en">
<head>
<meta charset="utf-8">
<title>Velsane Business Card</title>
<link rel="stylesheet" href="https://fonts.googleapis.com/css2?family=Delius&display=swap">
<style>
  :root {
    --backdrop: #fbe6f0;
    --magenta: #e6007e;
    --plum: #8c1457;
    --white: #ffffff;
    --ink: #1a1a1a;
    --stitch-pink: #f08cbf;
  }
  * { margin: 0; padding: 0; box-sizing: border-box; }
  html, body { width: 1200px; height: 900px; overflow: hidden; }
  body {
    background: var(--backdrop);
    font-family: "Delius", cursive;
    position: relative;
  }
  .card {
    position: absolute;
    width: 520px;
    height: 300px;
    box-shadow: 0 6px 18px rgba(140, 20, 87, 0.18);
  }
  /* Front: representative details */
  .card-front {
    left: 60px;
    top: 244px;
    background: var(--magenta);
    color: var(--white);
  }
  .card-front::before {
    content: "";
    position: absolute;
    inset: 9px;
    border: 1.5px dashed rgba(255, 255, 255, 0.8);
  }
  .brand-mark {
    position: absolute;
    left: 30px;
    top: 22px;
    display: flex;
    align-items: center;
    gap: 10px;
    font-size: 40px;
    line-height: 1;
  }
  .brand-square {
    width: 22px;
    height: 22px;
    background: var(--white);
  }
  .rep-name {
    position: absolute;
    left: 30px;
    top: 95px;
    font-size: 24px;
  }
  .rep-title {
    position: absolute;
    left: 42px;
    top: 128px;
    font-size: 15px;
    letter-spacing: 0.5px;
  }
  .contact-list {
    position: absolute;
    left: 30px;
    top: 198px;
    list-style: none;
    font-size: 17px;
    line-height: 31px;
  }
  /* Back: brand and tagline */
  .card-back {
    left: 620px;
    top: 352px;
    background: var(--white);
    border: 9px solid var(--magenta);
  }
  .card-back::before {
    content: "";
    position: absolute;
    inset: 7px;
    border: 1.5px dashed var(--stitch-pink);
  }
  .back-brand {
    position: absolute;
    left: 0;
    right: 0;
    top: 88px;
    display: flex;
    justify-content: center;
    align-items: center;
    gap: 16px;
    color: var(--magenta);
    font-size: 64px;
    line-height: 1;
  }
  .back-brand .brand-square {
    width: 34px;
    height: 34px;
    background: var(--plum);
  }
  .tagline {
    position: absolute;
    right: 26px;
    bottom: 22px;
    color: var(--ink);
    font-size: 22px;
  }
</style>
</head>
<body>
  <section class="card card-front" aria-label="Business card front">
    <div class="brand-mark"><span class="brand-square"></span><span class="brand-name">Velsane</span></div>
    <p class="rep-name">Dana Whitfield</p>
    <p class="rep-title">HFKDUHSNC</p>
    <ul class="contact-list">
      <li>www.myvelsane.example</li>
      <li>Phone: 1-800-472-Velsan</li>
      <li>Email: dana@myvelsane.example</li>
    </ul>
  </section>

  <section class="card card-back" aria-label="Business card back">
    <div class="back-brand"><span class="brand-square"></span><span class="brand-name">Velsane</span></div>
    <p class="tagline">Velsane is all about V</p>
  </section>
</body>
</html>
```